Creative design for PLW Businesscard!

We would like a creative business card for our company The Maple Workshop. We situated in Barcelona and setup software development teams for companies in Belgium, Holland.

Orange is related to Holland.
PLW means cool in Dutch

* An Overview / Background of the Business & Services
o Setup and manage developer teams in Barcelona for for companies
in Holland, Belgium.
* The Target Market / Audience you are trying to reach
o Companies in Holland searching for developers
* Design Specifics; any preferences or ideas for Style, Colour,
Imagery, etc
o Orange, professional, fancy
o The Maple Workshop (PLW) means cool , good, nice

Target Market(s)

Companies in Holland searching for developers

Industry/Entity Type

Business

Contact Information for Business Card

Company name: The Maple Workshop

Name: Joost ter Haarveld

Title: Managing director (not necessary)

Email: joost@themapleworkshop.es

web: www.themapleworkshop.es

Phone: (+34) 932 487 113

Mobile: (+34) 668 302 947

Font styles to use
Other font styles liked:
• Bookman Old Style or Rockwell

Requirements
Must have
• Setup and manage developer teams in Barcelona for for companies
• in Holland, Belgium.

```html
<!DOCTYPE html>
<html lang="en">
<head>
<meta charset="utf-8">
<title>PLW Business Card – The Maple Workshop</title>
<link rel="stylesheet" href="https://fonts.googleapis.com/css2?family=Arvo:wght@400;700&family=Open+Sans:wght@400;600&display=swap">
<style>
  :root {
    --charcoal: #3d3d3d;
    --ink: #333333;
    --orange: #d97236;
    --green: #3f8f3a;
    --paper: #ffffff;
    --backdrop: #e9e9e7;
  }
  * { box-sizing: border-box; margin: 0; padding: 0; }
  html, body { width: 1200px; height: 900px; overflow: hidden; }
  body {
    background: var(--backdrop);
    font-family: "Open Sans", Arial, sans-serif;
    position: relative;
  }
  .card {
    position: absolute;
    left: 260px;
    width: 680px;
    height: 390px;
    border-radius: 22px;
    overflow: hidden;
    box-shadow: 0 6px 18px rgba(0,0,0,.18);
  }
  .card-front { top: 40px; background: var(--charcoal); }
  .card-back { top: 470px; background: var(--paper); }
  .card-shapes { position: absolute; inset: 0; width: 100%; height: 100%; }

  .wordmark {
    position: absolute;
    font-family: "Arvo", Georgia, serif;
    font-weight: 700;
    letter-spacing: 4px;
    line-height: 1;
    display: flex;
    align-items: center;
    gap: 18px;
  }
  .wordmark-dot { border-radius: 50%; background: var(--orange); flex: none; }
  .card-front .wordmark { left: 0; right: 0; top: 110px; justify-content: center; font-size: 120px; color: var(--paper); }
  .card-front .wordmark-dot { width: 34px; height: 34px; }
  .card-back .wordmark { left: 48px; top: 80px; font-size: 86px; color: var(--ink); }
  .card-back .wordmark-dot { width: 24px; height: 24px; }

  .front-web {
    position: absolute; left: 34px; bottom: 18px;
    color: var(--paper); font-size: 17px; letter-spacing: .3px;
  }

  .person { position: absolute; right: 44px; top: 56px; text-align: right; }
  .person-name { font-family: "Arvo", Georgia, serif; color: var(--orange); font-size: 25px; }
  .person-title { font-family: "Arvo", Georgia, serif; color: var(--ink); font-size: 15px; margin-top: 2px; }

  .contacts { position: absolute; left: 50px; top: 248px; list-style: none; }
  .contacts li {
    display: flex; align-items: center; gap: 10px;
    font-size: 15px; color: var(--ink); line-height: 20px;
  }
  .contacts svg { width: 13px; height: 13px; flex: none; }
  .contacts .accent { color: var(--orange); }
</style>
</head>
<body>

<section class="card card-front" aria-label="Business card front">
  <svg class="card-shapes" viewBox="0 0 680 390" aria-hidden="true">
    <polygon points="395,352 680,300 680,320 395,372" fill="var(--paper)"/>
    <polygon points="0,332 372,332 410,352 410,390 0,390" fill="var(--orange)"/>
  </svg>
  <div class="wordmark"><span class="wordmark-dot"></span>PLW</div>
  <p class="front-web">www.themapleworkshop.es</p>
</section>

<section class="card card-back" aria-label="Business card back">
  <svg class="card-shapes" viewBox="0 0 680 390" aria-hidden="true">
    <line x1="50" y1="246" x2="640" y2="118" stroke="var(--green)" stroke-width="2"/>
    <polygon points="548,220 680,220 680,318 518,318" fill="var(--orange)"/>
    <polygon points="0,366 500,326 510,326 510,390 0,390" fill="var(--green)"/>
  </svg>

  <div class="wordmark"><span class="wordmark-dot"></span>PLW</div>

  <div class="person">
    <p class="person-name">Joost ter Haarveld</p>
    <p class="person-title">Managing director</p>
  </div>

  <ul class="contacts">
    <li>
      <svg viewBox="0 0 16 16"><path d="M3 1l3 3-2 2c1 2 3 4 5 5l2-2 3 3-2 3C7 15 1 9 1 3z" fill="var(--orange)"/></svg>
      (+34) 932 487 113
    </li>
    <li>
      <svg viewBox="0 0 16 16"><rect x="4" y="1" width="8" height="14" rx="1.5" fill="none" stroke="var(--orange)" stroke-width="1.6"/><circle cx="8" cy="12.3" r="1" fill="var(--orange)"/></svg>
      (+34) 668 302 947
    </li>
    <li>
      <svg viewBox="0 0 16 16"><rect x="1" y="3" width="14" height="10" fill="none" stroke="var(--orange)" stroke-width="1.6"/><path d="M1 3l7 6 7-6" fill="none" stroke="var(--orange)" stroke-width="1.6"/></svg>
      joost@themapleworkshop.es
    </li>
    <li>
      <svg viewBox="0 0 16 16"><circle cx="8" cy="8" r="6.5" fill="none" stroke="var(--orange)" stroke-width="1.4"/><ellipse cx="8" cy="8" rx="3" ry="6.5" fill="none" stroke="var(--orange)" stroke-width="1.2"/><path d="M1.5 8h13" stroke="var(--orange)" stroke-width="1.2"/></svg>
      <span>www.<span class="accent">themapleworkshop</span>.es</span>
    </li>
  </ul>
</section>

</body>
</html>
```